Sol Rumbo Coaching Services

My info is
Darsie Quenell-Abaro
darsie@solrumbocoaching.example
solrumbocoaching.example
555-413-7082

you can play with order of items. I've never had a letterhead before. Thank you!

```html
<!DOCTYPE html>
<html lang="en">
<head>
<meta charset="UTF-8">
<title>Sol Rumbo Coaching Services – Letterhead</title>
<link href="https://fonts.googleapis.com/css2?family=Arimo:wght@400;700&display=swap" rel="stylesheet">
<style>
  :root {
    --brand-red: #c1272d;
    --brand-orange: #f7931e;
    --ink: #231f20;
    --rule-grey: #b3b3b3;
    --paper: #ffffff;
  }
  html, body {
    margin: 0;
    padding: 0;
    width: 866px;
    height: 1200px;
    overflow: hidden;
    background: var(--paper);
  }
  .letterhead {
    position: relative;
    width: 866px;
    height: 1200px;
    background: var(--paper);
    font-family: "Arimo", Arial, sans-serif;
    overflow: hidden;
  }
  .corner-swoosh {
    position: absolute;
    top: 0;
    left: 0;
  }
  .brand-mark {
    position: absolute;
    top: 20px;
    left: 84px;
    width: 200px;
    text-align: center;
  }
  .brand-mark__dot {
    display: block;
    width: 64px;
    height: 64px;
    margin: 0 auto;
    border-radius: 50%;
    background: var(--brand-orange);
    box-shadow: 0 0 0 3px var(--paper), 0 0 0 4px var(--brand-red);
  }
  .brand-mark__name {
    display: block;
    margin-top: 14px;
    font-size: 34px;
    font-weight: 400;
    color: var(--brand-red);
    white-space: nowrap;
  }
  .masthead-title {
    position: absolute;
    top: 28px;
    left: 347px;
    margin: 0;
    font-size: 32px;
    font-weight: 700;
    color: var(--brand-red);
    white-space: nowrap;
  }
  .contact-block {
    position: absolute;
    top: 76px;
    left: 517px;
    margin: 0;
    font-style: normal;
    font-size: 17px;
    line-height: 21.5px;
    color: var(--ink);
  }
  .contact-block span { display: block; }
  .footer-band {
    position: absolute;
    left: 22px;
    right: 10px;
    bottom: 6px;
    display: flex;
    align-items: center;
    gap: 10px;
  }
  .footer-band__rule {
    flex: 1;
    height: 1px;
    background: var(--rule-grey);
  }
  .footer-band__name {
    font-size: 33px;
    font-weight: 700;
    color: var(--brand-orange);
    white-space: nowrap;
  }
</style>
</head>
<body>
  <div class="letterhead">
    <svg class="corner-swoosh" width="200" height="190" viewBox="0 0 200 190" aria-hidden="true">
      <path d="M0 0 H162 C100 12 40 40 0 92 Z" fill="var(--brand-orange)"/>
      <path d="M0 180 C20 100 70 38 160 0 L172 0 C90 34 30 96 0 150 Z" fill="var(--brand-red)"/>
    </svg>

    <div class="brand-mark">
      <span class="brand-mark__dot"></span>
      <span class="brand-mark__name">Sol Rumbo</span>
    </div>

    <h1 class="masthead-title">Sol Rumbo Coaching Services</h1>

    <address class="contact-block">
      <span>Darsie Quenell-Abaro</span>
      <span>email: darsie@solrumbocoaching.example</span>
      <span>www.solrumbocoaching.example</span>
      <span>Tel:555-413-7082</span>
    </address>

    <footer class="footer-band">
      <span class="footer-band__rule"></span>
      <span class="footer-band__name">Sol Rumbo Coaching Services</span>
      <span class="footer-band__rule"></span>
    </footer>
  </div>
</body>
</html>
```